Business card design for sustainable building and development company

Need a business card design for a new sustainable building and real estate development company in the San Francisco Bay area. Name of company is "HNX Consultants, LLC" and we provide "Sustainable building, energy and development services" for residential and non residential projects. We'd like the following colors used but not all area required: green, gray, blue. Design should communicate innovation, professionalism and sustainability. Our current website is www.hnx-consultants.com. Another possible design idea is to have the following listed on the back of the card:
Certified: TORV AP, Ecomark Rater, KWIL Rater, NovaTerra Inspector, DQX RT Building Analyst. Its not a must but could be text that could be used for back of card. Overall, we are open to a simple, clean design and or one with more text than usual for a card.

Industry/Entity Type

Real Estate

Contact Information for Business Card

Name on card: Derek M. Halvorsen
Title for Name: Principal + Founder
Phone: 650.555.0184
Email: dhalvorsen@hnx-consultants.com
Website: www.hnx-consultants.com

Also, please add the following for address:
San Francisco, California

Requirements
Nice to have
• If you can integrate the outline of a skyline on the backside of the card and if it looks good, I would like to see the design
Should not have
• a barcode;

```html
<!DOCTYPE html>
<html lang="en">
<head>
<meta charset="utf-8">
<title>HNX Consultants, LLC – Business Card</title>
<link rel="stylesheet" href="https://fonts.googleapis.com/css2?family=Abel&display=swap">
<style>
  :root {
    --paper: #ffffff;
    --ink: #4a4a4a;
    --brand-blue: #349fd9;
    --brand-green: #a0cb38;
    --rule-gray: #d9d9d9;
  }
  html, body {
    margin: 0;
    padding: 0;
    overflow: hidden;
    background: var(--paper);
  }
  .card {
    position: relative;
    width: 1200px;
    height: 678px;
    background: var(--paper);
    font-family: "Abel", "Arial Narrow", sans-serif;
    color: var(--ink);
    overflow: hidden;
  }
  .accent-square {
    position: absolute;
    left: 943px;
    top: 0;
    width: 116px;
    height: 179px;
    background: var(--brand-green);
  }
  .header-rule {
    position: absolute;
    left: 0;
    top: 161px;
    width: 943px;
    height: 18px;
    background: var(--rule-gray);
  }
  .side-bar {
    position: absolute;
    left: 0;
    top: 179px;
    width: 151px;
    height: 499px;
    background: var(--brand-blue);
  }
  .name,
  .title,
  .contact-line {
    position: absolute;
    margin: 0;
    line-height: 1;
    white-space: nowrap;
    font-weight: 400;
  }
  .name {
    left: 168px;
    top: 88px;
    font-size: 61px;
  }
  .title {
    left: 168px;
    top: 203px;
    font-size: 49px;
  }
  .contact-line {
    left: 178px;
    font-size: 40px;
  }
  .contact-phone { top: 417px; }
  .contact-email { top: 486px; }
  .contact-web {
    top: 560px;
    color: var(--brand-green);
  }
</style>
</head>
<body>
  <main class="card">
    <div class="accent-square"></div>
    <div class="header-rule"></div>
    <div class="side-bar"></div>

    <h1 class="name">Derek M. Halvorsen</h1>
    <p class="title">Principal/Owner</p>

    <p class="contact-line contact-phone">Phone: 650.555.0184</p>
    <p class="contact-line contact-email">Email: dhalvorsen@hnx-consultants.com</p>
    <p class="contact-line contact-web">www.hnx-consultants.com</p>
  </main>
</body>
</html>
```